Business Card Design Project

We require a business card template to cover basic contact information - our company logo, names of employees, title, mobile and email.

Target Market(s)

Corporate

Industry/Entity Type

Business

Font styles to use
Sans Serif

Requirements
Nice to have
• Thinking it would be great just to have the logo taking up approximately half the space (so it goes as far across the top of the card as possible) and then contact details in the lower half of the card. Keen just to use only the two colours in the logo, on a white background.
Should not have
• No fussy drawings

```html
<!DOCTYPE html>
<html lang="en">
<head>
<meta charset="utf-8">
<title>Tidewell Estates – Business Card</title>
<link rel="stylesheet" href="https://fonts.googleapis.com/css2?family=EB+Garamond:wght@500;700&display=swap">
<style>
  :root {
    --page-bg: #e4e6e8;
    --card-white: #f7f7f5;
    --brand-teal: #138a8a;
    --brand-navy: #1f3f86;
    --pattern-tint: #e9eeef;
    --text-light: #f2f4f6;
  }
  * { margin: 0; padding: 0; box-sizing: border-box; }
  html, body {
    width: 1200px;
    height: 945px;
    overflow: hidden;
    background: var(--page-bg);
    font-family: "EB Garamond", Garamond, serif;
  }
  .card {
    position: absolute;
    left: 100px;
    top: 186px;
    width: 1000px;
    height: 572px;
    background: var(--card-white);
    overflow: hidden;
    box-shadow: 0 6px 18px rgba(0,0,0,0.15);
  }
  .card__pattern {
    position: absolute;
    left: 0; top: 0;
    width: 100%;
    height: 330px;
    background: linear-gradient(100deg, var(--card-white) 0%, var(--pattern-tint) 50%, var(--card-white) 100%);
  }
  .card__brand {
    position: absolute;
    right: 60px;
    top: 120px;
    font-size: 112px;
    font-weight: 500;
    line-height: 1;
    color: var(--brand-teal);
    letter-spacing: -1px;
    white-space: nowrap;
  }
  .card__band {
    position: absolute;
    left: 0;
    top: 330px;
    width: 100%;
    height: 242px;
    background: linear-gradient(90deg, var(--brand-teal) 0%, var(--brand-navy) 62%, var(--brand-navy) 100%);
    color: var(--text-light);
    font-weight: 700;
  }
  .person {
    position: absolute;
    left: 52px;
    top: 32px;
    font-size: 30px;
    line-height: 1.3;
  }
  .contact {
    position: absolute;
    right: 52px;
    bottom: 30px;
    text-align: right;
    font-size: 34px;
    line-height: 1.3;
  }
</style>
</head>
<body>
  <main class="card">
    <div class="card__pattern" role="img" aria-label="Faint repeated company name background pattern"></div>
    <div class="card__brand">Tidewell Estates</div>
    <section class="card__band">
      <div class="person">
        <p class="person__name">Name Here</p>
        <p class="person__title">Property Manager</p>
      </div>
      <div class="contact">
        <p class="contact__phone">0-123-456789</p>
        <p class="contact__email">email@email.com</p>
      </div>
    </section>
  </main>
</body>
</html>
```